Wrenmoor Learning Houses MOXIE Poster

We need a poster to put up around our Community/Youth Centers that shows the acronym M.O.X.I.E. which stands for the traits our that make up the culture and personalities of our youth, families and staff. We would like the color scheme to be in our brand colors, and will send them as an upload (grey, blue, green). The poster must have our logo & tagline (uploaded), which may be small and not central. It should have the acronym with the associated words spelled out - as the smaller descriptive words as shown in uploaded attachment. It should be fun - youth friendly (ages 3-18) and really pop. I have also uploaded a sample poster that we created - but don't like....it feels boring, uninspired. It must say "The WLH" M.O.X.I.E as MOXIE is also the name of a different youth agency and we don't want our acronym to be confused with their name. Finally - to tell you a bit more about our organization I have uploaded our annual report. We can't way to see your ideas!!

Target Market(s)

Internal Information Poster for our community centers

Industry/Entity Type

Education

Font styles to use
Other font styles liked:
• FUN

Requirements
Must have
• It must say "The WLH" M.O.X.I.E as MOXIE is also the name of a different youth agency and we don't want our acronym to be confused with their name
• The WLH M.O.X.I.E. - and associated words - should be dominant/prevalent ....
Nice to have
• Fun Images/photos of actual sparks....
Should not have
• As described w/uploads

```html
<!DOCTYPE html>
<html lang="en">
<head>
<meta charset="utf-8">
<title>The WLH MOXIE Poster</title>
<link rel="stylesheet" href="https://fonts.googleapis.com/css2?family=Montserrat:wght@900&family=Fredoka:wght@600;700&family=Poppins:wght@400;500&display=swap">
<style>
  :root {
    --paper: #e9eaeb;
    --footer: #f3f3f3;
    --green-deep: #2fa64a;
    --green-light: #63c24a;
    --green-swoosh: #8fd66e;
    --teal: #2b8580;
    --teal-dark: #1d5e5c;
    --leaf: #5a9a3c;
    --leaf-dark: #3f7d2c;
    --slate: #505254;
    --rule: #8a8c8e;
    --white: #ffffff;
  }
  * { box-sizing: border-box; margin: 0; padding: 0; }
  html, body { width: 877px; height: 1200px; overflow: hidden; background: var(--paper); }
  .poster { position: relative; width: 877px; height: 1200px; background: var(--paper); overflow: hidden; }

  .header { position: absolute; left: 0; top: 0; width: 877px; height: 270px; }
  .header svg { position: absolute; inset: 0; }
  .title {
    position: absolute; left: 0; right: 0; top: 42px; text-align: center;
    font-family: "Montserrat", sans-serif; font-weight: 900; font-size: 128px;
    letter-spacing: 2px; color: var(--white); line-height: 1;
  }

  .burst {
    position: absolute; left: 90px; top: 250px; width: 720px; height: 860px;
    background: radial-gradient(ellipse at 50% 48%, rgba(255,255,255,0.7) 0%, rgba(255,255,255,0.25) 40%, rgba(255,255,255,0) 68%);
  }

  .traits { position: absolute; left: 68px; top: 302px; width: 740px; }
  .trait {
    position: relative; height: 148px;
    border-top: 1.5px solid var(--rule);
  }
  .trait:last-child { border-bottom: 1.5px solid var(--rule); }
  .trait::after {
    content: ""; position: absolute; left: 262px; top: 0; bottom: 0;
    border-left: 1.5px solid var(--slate);
  }
  .trait-notes {
    position: absolute; left: 58px; top: 38px; width: 200px;
    font-family: "Fredoka", sans-serif; font-weight: 600; font-size: 16.5px; line-height: 20.5px;
  }
  .trait-word {
    position: absolute; left: 310px; bottom: 10px;
    font-family: "Fredoka", sans-serif; font-weight: 700; white-space: nowrap; line-height: 0.8;
  }
  .trait-initial { font-size: 150px; }
  .trait-rest { font-size: 46px; margin-left: 2px; }

  .is-teal .trait-notes, .is-teal .trait-initial { color: var(--teal); }
  .is-teal .trait-rest { color: var(--teal-dark); }
  .is-leaf .trait-notes, .is-leaf .trait-initial { color: var(--leaf); }
  .is-leaf .trait-rest { color: var(--leaf-dark); }
  .is-slate .trait-notes, .is-slate .trait-initial, .is-slate .trait-rest { color: var(--slate); }

  .footer-rule { position: absolute; left: 0; top: 1078px; width: 877px; height: 6px; background: var(--leaf-dark); }
  .footer { position: absolute; left: 0; top: 1084px; width: 877px; height: 116px; background: var(--footer); }
  .brand { position: absolute; left: 168px; top: 30px; display: flex; align-items: center; gap: 12px; }
  .brand-dot { width: 40px; height: 40px; border-radius: 50%; background: var(--teal); flex: none; }
  .brand-text { font-family: "Poppins", sans-serif; }
  .brand-name { font-weight: 500; font-size: 27px; color: var(--teal); line-height: 1.1; letter-spacing: -0.3px; }
  .brand-tagline { font-weight: 400; font-size: 17px; color: var(--slate); letter-spacing: 1px; line-height: 1.3; }
</style>
</head>
<body>
<main class="poster">
  <header class="header">
    <svg width="877" height="270" viewBox="0 0 877 270" aria-hidden="true">
      <defs>
        <linearGradient id="header-fill" x1="0" y1="0" x2="1" y2="0">
          <stop offset="0" stop-color="var(--green-deep)"/>
          <stop offset="1" stop-color="var(--green-light)"/>
        </linearGradient>
      </defs>
      <path d="M0,0 H877 V85 C780,215 560,265 330,240 C190,225 80,195 0,160 Z" fill="url(#header-fill)"/>
      <path d="M0,140 C150,180 300,215 470,222 C640,228 780,170 877,92" fill="none" stroke="var(--green-swoosh)" stroke-width="6" opacity="0.7"/>
      <path d="M0,175 C160,220 330,255 500,250 C660,245 790,180 877,120" fill="none" stroke="var(--green-swoosh)" stroke-width="3" opacity="0.5"/>
    </svg>
    <h1 class="title">THE WLH</h1>
  </header>

  <div class="burst" role="img" aria-label="Faint white firework burst behind the trait list"></div>

  <section class="traits">
    <div class="trait is-teal">
      <p class="trait-notes">Warm &amp; Welcoming<br>Confident<br>Communicator<br>Positive Attitude</p>
      <p class="trait-word"><span class="trait-initial">M</span><span class="trait-rest">otivated</span></p>
    </div>
    <div class="trait is-leaf">
      <p class="trait-notes">Persistent Goal<br>Oriented Engaged<br>Creative Innovator</p>
      <p class="trait-word"><span class="trait-initial">O</span><span class="trait-rest">ptimistic</span></p>
    </div>
    <div class="trait is-slate">
      <p class="trait-notes">Resilient<br>Resourceful<br>Willing<br>Critical Thinker</p>
      <p class="trait-word"><span class="trait-initial">X</span><span class="trait-rest">plorer</span></p>
    </div>
    <div class="trait is-teal">
      <p class="trait-notes">Accountable<br>Committed<br>Self-Regulating</p>
      <p class="trait-word"><span class="trait-initial">I</span><span class="trait-rest">ntentional</span></p>
    </div>
    <div class="trait is-leaf">
      <p class="trait-notes">Empathetic<br>Collaborative<br>Helpful</p>
      <p class="trait-word"><span class="trait-initial">E</span><span class="trait-rest">mpathetic</span></p>
    </div>
  </section>

  <div class="footer-rule"></div>
  <footer class="footer">
    <div class="brand">
      <span class="brand-dot"></span>
      <div class="brand-text">
        <p class="brand-name">WRENMOOR LEARNING HOUSES</p>
        <p class="brand-tagline">WHERE CURIOSITY GROWS</p>
      </div>
    </div>
  </footer>
</main>
</body>
</html>
```